Business Cards & Stationary for Solo Attorney
Marcus Tolland Counsellor At Law
Business Cards & Stationary for Solo Attorney - Law
Creative Brief
Professional
Marcus Tolland
Counsellor At Law
482 Brindlecombe Avenue, 5th Floor Harwick Falls, Vermont 08347
mtollandlaw@quillpost.example
tollandlawfirm.example

```html
<!DOCTYPE html>
<html lang="en">
<head>
<meta charset="utf-8">
<title>Marcus Tolland Counsellor At Law – Stationery Set</title>
<link rel="stylesheet" href="https://fonts.googleapis.com/css2?family=Cinzel:wght@500;700&family=Open+Sans:wght@400;600;700&display=swap">
<style>
  :root{
    --navy:#1d2b50;
    --navy-deep:#15203d;
    --khaki:#b9a57a;
    --paper:#ffffff;
    --ink:#2b2f3a;
    --rule:#c9ccd4;
    --mark:#e3e5ea;
    --mark-on-navy:#2b3a62;
    --stage:#e9e6e1;
  }
  *{box-sizing:border-box;margin:0;padding:0}
  html,body{width:1200px;height:514px;overflow:hidden}
  body{background:var(--stage);position:relative;font-family:"Open Sans",sans-serif;color:var(--ink)}
  .sheet{position:absolute;background:var(--paper);box-shadow:0 2px 6px rgba(0,0,0,.18);overflow:hidden}

  .brand{position:absolute;display:flex;align-items:center;gap:6px;color:var(--navy);font-family:"Cinzel",serif;font-weight:700}
  .brand__dot{border-radius:50%;background:var(--navy);flex:none}
  .brand__name{line-height:1.05;letter-spacing:.04em;white-space:nowrap}
  .brand__name small{display:block;font-size:.55em;letter-spacing:.12em}
  .brand--light{color:#fff}
  .brand--light .brand__dot{background:#fff}

  .watermark{position:absolute;border-radius:50%;background:var(--mark)}

  .footer-band{position:absolute;left:0;right:0;bottom:0}
  .footer-band__stripe{height:4px;background:var(--khaki)}
  .footer-band__bar{background:var(--navy);color:#fff;font-size:5px;letter-spacing:.05em;display:flex;align-items:center;padding-left:14px;white-space:nowrap}

  /* letterhead */
  .letterhead{left:20px;top:38px;width:340px;height:432px}
  .letterhead .contact{position:absolute;right:16px;top:16px;font-size:5px;line-height:1.6}

  /* fax */
  .fax{left:384px;top:38px;width:336px;height:432px}
  .fax__title{position:absolute;left:18px;top:56px;font-size:20px;font-weight:700;color:var(--ink)}
  .fax__form{position:absolute;left:18px;top:100px;width:300px;display:grid;grid-template-columns:1fr 1fr;column-gap:14px;row-gap:9px;font-size:5.5px}
  .fax__field{display:flex;gap:4px;border-bottom:1px solid var(--rule);padding-bottom:2px}
  .fax__checks{position:absolute;left:18px;top:180px;width:300px;display:flex;justify-content:space-between;font-size:5px}
  .fax__checks span{display:flex;align-items:center;gap:3px}
  .fax__checks span::before{content:"";width:5px;height:5px;border:1px solid var(--ink)}

  /* business cards */
  .card{top:100px;height:104px}
  .card--front{left:738px;width:214px}
  .card--front .card__band{position:absolute;left:0;right:0;top:54px;height:9px;background:var(--navy);color:#fff;font-size:5px;display:flex;align-items:center;padding-left:10px;white-space:nowrap}
  .card--front .card__contact{position:absolute;left:10px;top:68px;font-size:5px;line-height:1.6}
  .card--back{left:964px;width:220px;background:var(--navy)}
  .card--back .watermark{background:var(--mark-on-navy)}
  .card__site{position:absolute;right:12px;bottom:10px;color:#fff;font-size:6px}

  /* envelope back */
  .envelope-back{left:738px;top:218px;width:446px;height:140px}
  .envelope-back svg{position:absolute;left:0;top:0}

  /* envelope front */
  .envelope-front{left:738px;top:366px;width:446px;height:104px}
  .envelope-front .return{position:absolute;left:14px;top:34px;font-size:4.5px;line-height:1.5}
  .envelope-front .footer-band__bar{height:12px;justify-content:center;padding:0}
</style>
</head>
<body>

<section class="sheet letterhead">
  <div class="brand" style="left:16px;top:14px;font-size:9px">
    <span class="brand__dot" style="width:16px;height:16px"></span>
    <span class="brand__name">Marcus Tolland<small>Counsellor At Law</small></span>
  </div>
  <div class="contact">
    <div>(555) 214-0148</div>
    <div>(555) 214-0149</div>
    <div>mtollandlaw@quillpost.example</div>
  </div>
  <div class="watermark" style="left:70px;top:80px;width:200px;height:200px"></div>
  <div class="footer-band">
    <div class="footer-band__stripe"></div>
    <div class="footer-band__bar" style="height:14px">482 Brindlecombe Avenue, 5th Floor, Harwick Falls, Vermont 08347 &nbsp;•&nbsp; (555) 214-0148 &nbsp;•&nbsp; tollandlawfirm.example</div>
  </div>
</section>

<section class="sheet fax">
  <div class="brand" style="left:16px;top:14px;font-size:9px">
    <span class="brand__dot" style="width:16px;height:16px"></span>
    <span class="brand__name">Marcus Tolland<small>Counsellor At Law</small></span>
  </div>
  <h1 class="fax__title">FAX</h1>
  <div class="fax__form">
    <div class="fax__field">To:</div><div class="fax__field">Date:</div>
    <div class="fax__field">Fr:</div><div class="fax__field">Pages:</div>
    <div class="fax__field">Phone:</div><div class="fax__field">Fax:</div>
    <div class="fax__field">Re:</div><div class="fax__field">CC:</div>
  </div>
  <div class="fax__checks">
    <span>Urgent</span><span>For Review</span><span>Please Comment</span><span>Please Reply</span><span>Please Recycle</span>
  </div>
  <div class="footer-band">
    <div class="footer-band__stripe"></div>
    <div class="footer-band__bar" style="height:14px">482 Brindlecombe Avenue, 5th Floor, Harwick Falls, Vermont 08347 &nbsp;•&nbsp; (555) 214-0148 &nbsp;•&nbsp; tollandlawfirm.example</div>
  </div>
</section>

<section class="sheet card card--front">
  <div class="brand" style="left:10px;top:12px;font-size:10px">
    <span class="brand__dot" style="width:18px;height:18px"></span>
    <span class="brand__name">Marcus Tolland<small>Counsellor At Law</small></span>
  </div>
  <div class="card__band">(555) 214-0148 &nbsp;•&nbsp; mtollandlaw@quillpost.example</div>
  <div class="card__contact">
    <div>482 Brindlecombe Avenue, 5th Floor</div>
    <div>Harwick Falls, Vermont 08347</div>
  </div>
</section>

<section class="sheet card card--back">
  <div class="watermark" style="left:88px;top:8px;width:44px;height:44px"></div>
  <div class="brand brand--light" style="left:0;right:0;top:56px;justify-content:center;font-size:15px">
    <span class="brand__name">Marcus Tolland</span>
  </div>
  <div class="card__site">tollandlawfirm.example</div>
</section>

<section class="sheet envelope-back">
  <svg width="446" height="140" viewBox="0 0 446 140">
    <polyline points="0,140 190,76" fill="none" stroke="var(--rule)" stroke-width="1"/>
    <polyline points="446,140 256,76" fill="none" stroke="var(--rule)" stroke-width="1"/>
    <polygon points="0,0 446,0 223,92" fill="var(--navy)"/>
  </svg>
  <div class="brand brand--light" style="left:0;right:0;top:22px;justify-content:center;flex-direction:column;gap:3px;font-size:9px;text-align:center">
    <span class="brand__dot" style="width:18px;height:18px"></span>
    <span class="brand__name">Marcus Tolland<small>Counsellor At Law</small></span>
  </div>
</section>

<section class="sheet envelope-front">
  <div class="brand" style="left:14px;top:10px;font-size:8px">
    <span class="brand__dot" style="width:14px;height:14px"></span>
    <span class="brand__name">Marcus Tolland<small>Counsellor At Law</small></span>
  </div>
  <div class="return">
    <div>482 Brindlecombe Avenue, 5th Floor</div>
    <div>Harwick Falls, Vermont 08347</div>
  </div>
  <div class="watermark" style="right:30px;top:6px;width:78px;height:78px"></div>
  <div class="footer-band">
    <div class="footer-band__bar">tollandlawfirm.example</div>
  </div>
</section>

</body>
</html>
```